Flyer Design for sewing business

Hi. i need flyers for my new business called " Telvo Designs". I am based in Sauchie. I offer Door to Door Clothing Alteration Service!
I provide a door to door alteration service for Clackmannanshire area with 20 miles radiance! (I give free consultations at your preferred location where I can accurately quote the cost of the alteration, as this depends on the garment itself. I aim to deliver the completed item back to you within a week though often it is less than this.)
I also design and sew occasional girls dresses ( first communion, flower girl, party dresses)
The consultation are free with no commitment to take the service.

I wold like see designs that use colors similar to colors on my website, like dusty pink, orange.

To contact either phone RUTH 07913284406
or email: ruth.marsk71@quillbox.com

www.pagebook.com/telvodesigns
www.telvo-designs.sitenest.com

THAT IS THE Price List Jeans/Trousers: Shorten....................................from £10.00 Taken in (waist).......................from £8.00 Taken in (side seams)..............from £10.00 Replace zip...............................from £10.00 Dresses/Skirts: Shorten....................................from £10.00 Taken in (waist).......................from £8.00 Taken in (side seams)..............from £8.00 Replace zip...............................from £10.00 Jacket/Coat: Shorten sleeves........................from £12.00 Shorten length (Jacket)...........from £16.00 Shorten length (Coat)..............from £18.00 Taken in (back seam)...............from £12.00 Taken in (side seams)..............from £18.00 Repairs......................................from £5.00 Bridal: Shorten Wedding Dress...........from £25.00 All other bridal alteration quotes can be given on consultation.

Reason: HI, ALL! IN THE NEXT FEW DAYS I GONE EXPERIENCE HOUSE MOVE AND SOME STRESS INVOLVING IN THIS.THANK YOU ALL FOR UNDERSTANDING AND A PATIENCE!

Industry/Entity Type

Business

```html
<!DOCTYPE html>
<html lang="en">
<head>
<meta charset="UTF-8">
<title>Telvo Designs – Price List</title>
<link href="https://fonts.googleapis.com/css2?family=Playfair+Display:wght@700&family=Open+Sans:wght@300;400&family=Cinzel:wght@700&display=swap" rel="stylesheet">
<style>
  :root {
    --paper: #fbe6dc;
    --rose: #c9587b;
    --rose-soft: #d98aa2;
    --button: #e7a9b6;
    --ink: #5e4a4e;
    --dash: #d5a0ad;
    --white: #ffffff;
  }
  html, body { margin: 0; padding: 0; overflow: hidden; }
  body { width: 851px; height: 1200px; background: var(--paper); }
  .flyer {
    position: relative;
    width: 851px; height: 1200px;
    background: var(--paper);
    overflow: hidden;
    font-family: "Open Sans", Arial, sans-serif;
    color: var(--ink);
  }
  .flyer-frame {
    position: absolute; inset: 20px;
    border: 2px dashed var(--dash);
    border-radius: 6px;
  }
  .title {
    position: absolute; top: 22px; left: 0; right: 0;
    margin: 0; text-align: center;
    font-family: "Playfair Display", Georgia, serif;
    font-weight: 700; font-size: 54px; color: var(--rose);
  }
  .price-list {
    position: absolute; left: 218px; width: 412px;
    font-weight: 300;
  }
  .price-group h2 {
    margin: 0; text-align: center;
    font-weight: 300; font-size: 25px; line-height: 30px; color: var(--ink);
  }
  .price-row {
    display: flex; font-size: 21px; line-height: 23px; white-space: nowrap;
  }
  .price-row .item { flex: none; }
  .price-row .leader { flex: 1; min-width: 40px; overflow: hidden; letter-spacing: 1px; }
  .price-row .leader::before { content: "........................................................................................"; }
  .price-row .cost { flex: none; }
  .price-row.bridal-row { width: 410px; margin: 0 auto; font-size: 20px; }
  .bridal-note {
    position: absolute; top: 624px; left: 0; right: 0;
    text-align: center; font-size: 20px; font-weight: 300; margin: 0;
  }
  .photo {
    position: absolute; border: 5px solid var(--white);
    box-shadow: 0 3px 8px rgba(0,0,0,.25);
  }
  .photo-dress {
    left: 62px; top: 668px; width: 262px; height: 300px;
    background: linear-gradient(160deg, #b7a59c 0%, #e9dfe0 45%, #f4eef0 70%, #d9c6bf 100%);
    transform: rotate(-2deg);
  }
  .photo-sash {
    left: 340px; top: 664px; width: 320px; height: 236px;
    background: linear-gradient(135deg, #f3a9c4 0%, #ec89ad 50%, #f6bcd0 100%);
    transform: rotate(2deg);
  }
  .consult-badge {
    position: absolute; left: 486px; top: 829px; width: 210px; height: 210px;
  }
  .consult-badge text {
    font-family: "Cinzel", Georgia, serif; font-weight: 700; font-size: 17px;
    fill: var(--white);
  }
  .footer-note {
    position: absolute; top: 1052px; left: 30px; right: 30px; margin: 0;
    text-align: center; font-size: 16px; line-height: 30px; font-weight: 400;
    white-space: nowrap;
  }
  .decor { position: absolute; }
</style>
</head>
<body>
<main class="flyer">
  <div class="flyer-frame"></div>

  <svg class="decor" style="left:100px;top:155px" width="56" height="56" role="img" aria-label="Decorative sewing button">
    <circle cx="28" cy="28" r="27" fill="var(--button)"/>
  </svg>
  <svg class="decor" style="left:70px;top:275px" width="34" height="34" role="img" aria-label="Decorative sewing button">
    <circle cx="17" cy="17" r="16" fill="var(--button)"/>
  </svg>
  <svg class="decor" style="left:640px;top:180px" width="130" height="130" role="img" aria-label="Decorative flower">
    <circle cx="65" cy="65" r="62" fill="var(--rose-soft)"/>
  </svg>
  <svg class="decor" style="left:735px;top:120px" width="36" height="36" role="img" aria-label="Decorative sewing button">
    <circle cx="18" cy="18" r="17" fill="var(--button)"/>
  </svg>
  <svg class="decor" style="left:50px;top:395px" width="140" height="140" role="img" aria-label="Decorative flower">
    <circle cx="70" cy="70" r="67" fill="var(--rose-soft)"/>
  </svg>
  <svg class="decor" style="left:640px;top:405px" width="56" height="56" role="img" aria-label="Decorative sewing button">
    <circle cx="28" cy="28" r="27" fill="var(--button)"/>
  </svg>
  <svg class="decor" style="left:640px;top:515px" width="36" height="36" role="img" aria-label="Decorative sewing button">
    <circle cx="18" cy="18" r="17" fill="var(--button)"/>
  </svg>

  <h1 class="title">Price List</h1>

  <section class="price-list price-group" style="top:96px">
    <h2>Jeans/Trousers:</h2>
    <div class="price-row"><span class="item">Shorten</span><span class="leader"></span><span class="cost">from £10.00</span></div>
    <div class="price-row"><span class="item">Taken in (waist)</span><span class="leader"></span><span class="cost">from £8.00</span></div>
    <div class="price-row"><span class="item">Taken in (side seams)</span><span class="leader"></span><span class="cost">from £10.00</span></div>
    <div class="price-row"><span class="item">Replace zip</span><span class="leader"></span><span class="cost">from £10.00</span></div>
  </section>

  <section class="price-list price-group" style="top:262px">
    <h2>Dresses/Skirts:</h2>
    <div class="price-row"><span class="item">Shorten</span><span class="leader"></span><span class="cost">from £10.00</span></div>
    <div class="price-row"><span class="item">Taken in (waist)</span><span class="leader"></span><span class="cost">from £8.00</span></div>
    <div class="price-row"><span class="item">Taken in (side seams)</span><span class="leader"></span><span class="cost">from £8.00</span></div>
    <div class="price-row"><span class="item">Replace zip</span><span class="leader"></span><span class="cost">from £10.00</span></div>
  </section>

  <section class="price-list price-group" style="top:400px">
    <h2>Jacket/Coat:</h2>
    <div class="price-row"><span class="item">Shorten sleeves</span><span class="leader"></span><span class="cost">from £12.00</span></div>
    <div class="price-row"><span class="item">Shorten length (Jacket)</span><span class="leader"></span><span class="cost">from £16.00</span></div>
    <div class="price-row"><span class="item">Shorten length (Coat)</span><span class="leader"></span><span class="cost">from £18.00</span></div>
    <div class="price-row"><span class="item">Taken in (back seam)</span><span class="leader"></span><span class="cost">from £12.00</span></div>
    <div class="price-row"><span class="item">Taken in (side seams)</span><span class="leader"></span><span class="cost">from £18.00</span></div>
    <div class="price-row"><span class="item">Repairs</span><span class="leader"></span><span class="cost">from £5.00</span></div>
  </section>

  <section class="price-list price-group" style="top:566px">
    <h2>Bridal:</h2>
    <div class="price-row bridal-row"><span class="item">Shorten Wedding Dress</span><span class="leader"></span><span class="cost">from £25.00</span></div>
  </section>
  <p class="bridal-note">All other bridal alteration quotes can be given on consultation.</p>

  <div class="photo photo-dress" role="img" aria-label="Photo of a girl's white party dress with a pink sash"></div>
  <div class="photo photo-sash" role="img" aria-label="Photo of a pink satin dress bodice with a bow"></div>

  <svg class="consult-badge" viewBox="0 0 210 210">
    <circle cx="105" cy="105" r="104" fill="var(--rose)"/>
    <circle cx="105" cy="105" r="94" fill="none" stroke="var(--white)" stroke-width="2" stroke-dasharray="5 4"/>
    <text x="105" y="100" text-anchor="middle">FREE</text>
    <text x="105" y="124" text-anchor="middle" textLength="150" lengthAdjust="spacingAndGlyphs">CONSULTATIONS</text>
  </svg>

  <p class="footer-note">Door to door alteration service for Clackmannanshire area with 20 miles radiance!<br>Free consultations at your preferred location to accurately quote the cost of the alteration,<br>as this depends on the garment itself.</p>
</main>
</body>
</html>
```